1-3 PAGE WEBSITE LANDING PAGE DESIGN FOR REELPITCH.NET

I NEED A DESIGNER THAT HAS A GOOD UNDERSTANDING OF BUSINESS AND MARKETING SO HE CAN TAKE MY SALES SCRIPT AND CONVERT IT INTO A BEAUTIFUL IMAGE AND VIDEO FILLED WEBSITE THAT EXPLAINS EACH POINT BEAUTIFULLY. THE WEBSITE SHOULD BE EASY TO READ AND UNDERSTAND AND NAVIGATE.

PLEASE INCLUDE A EXAMPLES SECTION THAT CAN BE FILTERED BY INDUSTRY.

UNDER EVERY SECTION ON THE WEBSITE WE NEED TO HAVE A CALL TO ACTION BUTTON THAT WILL POP UP INTO A LEAD GEN FORM. THE BUTTON WILL SAY "SIGN UP FOR A FREE VIDEO AD MOCK UP FOR YOUR BUSINESS. No Purchase Necessary."

PLEASE SEE ATTACHED FILES FOR WORD DOC OF CONTENT AND LOGO FOR REELPITCH.NET

Target Market(s)

ALL BUSINESSES WHO WILL BE USING VIDEO ADVERTISEMENT AS PART OF THEIR OVERALL MARKETING STRATEGY FOR YEARS TO COME

Industry/Entity Type

Digital Marketing

Number of Pages Required

2 page

Colors

Designer to choose colors to be used in the design.

Requirements
Must have
• I would like color theme to coordinate with logo color theme
Nice to have
• must include all content included in word document

```html
<!DOCTYPE html>
<html lang="en">
<head>
<meta charset="utf-8">
<title>ReelPitch.net – Video Ads</title>
<link href="https://fonts.googleapis.com/css2?family=Poppins:wght@400;500;600;700&display=swap" rel="stylesheet">
<style>
:root{
  --yellow:#fcee33;
  --accent:#f7a51c;
  --ink:#111111;
  --text:#444444;
  --white:#ffffff;
  --dark:#1d1d1f;
  --soft:#f4f4f4;
}
*{margin:0;padding:0;box-sizing:border-box}
html,body{width:1200px;height:3606px;overflow:hidden}
body{font-family:'Poppins',sans-serif;color:var(--text);background:var(--white);position:relative}
section,header,footer{position:absolute;left:0;width:1200px}
.abs{position:absolute}
.center{left:0;width:1200px;text-align:center}
.underline{position:absolute;left:572px;width:56px;height:3px;background:var(--yellow)}

/* hero */
.hero{top:0;height:657px;background:linear-gradient(120deg,#1a2330 0%,#2a3038 40%,#1c2a38 70%,#0f151c 100%)}
.hero-photo{position:absolute;inset:0;background:radial-gradient(ellipse at 30% 45%,rgba(110,90,80,.45),transparent 55%),radial-gradient(ellipse at 80% 40%,rgba(60,110,150,.35),transparent 50%)}
.brand{position:absolute;font-weight:600;font-size:29px;color:var(--accent);letter-spacing:1px}
.nav{position:absolute;top:58px;left:476px;display:flex;gap:29px;font-size:12.5px;color:var(--white)}
.search{position:absolute;left:1003px;top:56px}
.hero h1{top:268px;font-size:42px;font-weight:700;color:var(--white)}
.hero .lead{top:334px;font-size:13px;color:var(--white)}
.btn{position:absolute;height:45px;border-radius:23px;font-size:12.5px;display:flex;align-items:center;justify-content:center}
.btn-yellow{background:var(--yellow);color:var(--ink)}
.btn-dark{background:var(--ink);color:var(--white)}

/* offer */
.offer{top:657px;height:634px}
h2{font-size:33px;font-weight:700;color:var(--ink)}
.offer-art{left:189px;top:190px;width:357px;height:350px;border-radius:6px;background:linear-gradient(135deg,#fdf1d8,#e9eef2)}
.offer-item h3{font-size:24px;font-weight:600;color:var(--ink)}
.offer-item p{font-size:12.5px;line-height:28px;margin-top:14px}

/* features */
.features{top:1291px;height:455px;background:linear-gradient(110deg,#121d28,#1f2b38 50%,#0e1822)}
.features h2{color:var(--white)}
.feature{position:absolute;top:196px;width:230px;text-align:center;color:var(--white)}
.feature svg{display:block;margin:0 auto}
.feature h4{font-size:16px;font-weight:600;margin-top:22px}
.feature p{font-size:12.5px;line-height:20px;margin-top:16px;color:#e4e4e4}

/* donate */
.donate{top:1746px;height:263px;background:var(--yellow)}
.donate .underline{background:var(--ink)}

/* promo */
.promo{top:2009px;height:570px}
.promo-copy{left:158px;top:213px;width:500px;font-size:12px;line-height:32px;white-space:nowrap}
.photo-back{left:778px;top:167px;width:257px;height:256px;background:linear-gradient(135deg,#3b3a3a,#6b5a4e 50%,#202428)}
.photo-front{left:661px;top:253px;width:256px;height:255px;background:linear-gradient(135deg,#2a3542,#5a6470 50%,#1a2028)}

/* team */
.team{top:2579px;height:654px;background:var(--soft)}
.team .intro{top:142px;font-size:12.5px;line-height:27px}
.card{position:absolute;top:225px;width:290px;text-align:center}
.card .photo{height:241px}
.card h5{font-size:16px;font-weight:600;color:var(--ink);margin-top:14px}
.card .role{font-size:12.5px;margin-top:4px}
.card.active{background:#222222;height:360px}
.card.active h5,.card.active .role{color:var(--white)}
.socials{display:flex;justify-content:center;gap:14px;margin-top:14px}
.dot{width:16px;height:16px;border-radius:50%;background:var(--white)}

/* footer */
.footer{top:3233px;height:324px;background:var(--dark)}
.footer .brand{top:86px;left:0;width:1200px;text-align:center}
.footer-nav{position:absolute;top:168px;left:0;width:1200px;display:flex;justify-content:center;gap:30px;font-size:12.5px;color:var(--white)}
.footer-social{position:absolute;top:229px;left:0;width:1200px;display:flex;justify-content:center;gap:24px}
.footer-social span{width:33px;height:33px;border-radius:50%;background:var(--white)}
.legal{top:3557px;height:49px;background:var(--yellow);font-size:12px;color:var(--ink);display:flex;align-items:center;justify-content:center}
</style>
</head>
<body>

<header class="hero">
  <div class="hero-photo" role="img" aria-label="Photo of a video team working at computer monitors in a dim studio"></div>
  <div class="brand" style="left:161px;top:40px">REELPITCH.NET</div>
  <nav class="nav"><span>Home</span><span>Features</span><span>Portfolio</span><span>News</span><span>Team</span><span>Products</span><span>Contact Us</span></nav>
  <svg class="search" width="18" height="18" viewBox="0 0 18 18" fill="none" stroke="#fff" stroke-width="1.6"><circle cx="7.5" cy="7.5" r="6"/><path d="M12 12l5 5"/></svg>
  <h1 class="abs center">Best Choice is ReelPitch</h1>
  <p class="abs center lead">We are a video production company that specializes in short, entertaining mini commercial type of video</p>
  <a class="btn btn-yellow" style="left:347px;top:389px;width:506px">Sign Up For a free video ad mockup for your business.No Purchase Necessary</a>
</header>

<section class="offer">
  <h2 class="abs center" style="top:55px">What We Can Offer</h2>
  <div class="underline" style="top:108px"></div>
  <div class="abs offer-art" role="img" aria-label="Illustration of a monitor with a play button, gears, books and a person at a desk"></div>
  <div class="abs offer-item" style="left:585px;top:168px"><h3>Production</h3><p>Ut bibendum justo luctus, viverra augue id, imperdiet tellus.<br>.Nullam sed nulla lacus</p></div>
  <div class="abs offer-item" style="left:619px;top:313px"><h3>Design</h3><p>Ut bibendum justo luctus, viverra augue id, imperdiet tellus.<br>.Nullam sed nulla lacus</p></div>
  <div class="abs offer-item" style="left:655px;top:460px"><h3>Marketing</h3><p>Ut bibendum justo luctus, viverra augue id, imperdiet tellus.<br>.Nullam sed nulla lacus</p></div>
</section>

<section class="features" role="img" aria-label="Dark background photo of an editor with headphones at a monitor">
  <h2 class="abs center" style="top:65px">Our Features</h2>
  <div class="underline" style="top:124px"></div>
  <div class="feature" style="left:131px">
    <svg width="52" height="50" viewBox="0 0 52 50" fill="none" stroke="#fff" stroke-width="2"><path d="M26 3l10 5v11l-10 5-10-5V8z"/><path d="M15 25l10 5v11l-10 5-10-5V30z"/><path d="M37 25l10 5v11l-10 5-10-5V30z"/></svg>
    <h4>Maticulously Crafted</h4><p>Fusce laoreet massa sed<br>metus cursus dapibus.<br>Aliquam erat volutpat.</p>
  </div>
  <div class="feature" style="left:368px">
    <svg width="52" height="50" viewBox="0 0 52 50" fill="none" stroke="#fff" stroke-width="2.4"><path d="M26 2l19 7v14c0 13-9 21-19 25C16 44 7 36 7 23V9z"/><circle cx="26" cy="25" r="10"/><path d="M21 25l4 4 7-8"/></svg>
    <h4>Fast and Secure</h4><p>Fusce laoreet massa sed<br>metus cursus dapibus.<br>Aliquam erat volutpat.</p>
  </div>
  <div class="feature" style="left:602px">
    <svg width="52" height="50" viewBox="0 0 52 50" fill="none" stroke="#fff" stroke-width="2"><rect x="5" y="24" width="9" height="20"/><path d="M14 26l9-10 3-10c4 0 5 4 4 9l-1 5h12c3 0 4 3 3 5l-4 16c-1 2-2 3-4 3H14"/><path d="M38 4v6M46 8l-4 4M48 16h-5"/></svg>
    <h4>Top Notch Quailty</h4><p>Fusce laoreet massa sed<br>metus cursus dapibus.<br>Aliquam erat volutpat.</p>
  </div>
  <div class="feature" style="left:838px">
    <svg width="52" height="50" viewBox="0 0 52 50"><path d="M26 2l20 6v16c0 12-9 21-20 25C15 45 6 36 6 24V8z" fill="#fff"/><path d="M26 8v34c-8-4-14-10-14-18V12z" fill="#1f2b38"/></svg>
    <h4>Incredilbly Smart</h4><p>Fusce laoreet massa sed<br>metus cursus dapibus.<br>Aliquam erat volutpat.</p>
  </div>
</section>

<section class="donate">
  <h2 class="abs center" style="top:36px">Donate for your Content</h2>
  <div class="underline" style="top:99px"></div>
  <p class="abs center" style="top:127px;font-size:12.5px;color:var(--ink)">.You can provide the content or we can come up with content for you. This really is a "done for you" service</p>
  <a class="btn btn-dark" style="left:347px;top:178px;width:506px">Sign Up For a free video ad mockup for your business.No Purchase Necessary</a>
</section>

<section class="promo">
  <h2 class="abs center" style="top:58px">Video Ads for Promoting your Special Offers</h2>
  <div class="underline" style="top:117px"></div>
  <p class="abs promo-copy">We are a video production company that specializes in short, entertaining mini<br>commercial type of video "ADS" ("ADVERTISEMENTS") FULLY CUSTOMIZED AND<br>BRANDED TO YOUR BUSINESS, using premium stock footage. Our video ads grab<br>attention within just a few seconds and get the call to action across quickly<br>such as clicking through to your website and opting into a webform or simply<br>.contacting your business</p>
  <a class="btn btn-yellow" style="left:158px;top:427px;width:132px;height:36px;font-size:12px">Read More</a>
  <div class="abs photo-back" role="img" aria-label="Photo of a camera operator filming in a studio"></div>
  <div class="abs photo-front" role="img" aria-label="Photo of a woman editing video at a desk with monitors"></div>
</section>

<section class="team">
  <h2 class="abs center" style="top:55px">Meet Our Team</h2>
  <div class="underline" style="top:113px;background:var(--ink)"></div>
  <p class="abs center intro">Cras nec cursus eros. Praesent lectus metus, dignissim ac diam malesuada, eleifend sollicitudin<br>.lacus. Aliquam erat volutpat. Maecenas id convallis nisi</p>
  <div class="card" style="left:141px">
    <div class="photo" role="img" aria-label="Portrait photo of a team member writing at a laptop" style="background:linear-gradient(135deg,#6b6660,#2f4a3a)"></div>
    <h5>Liam Carter</h5><div class="role">Co-Founder</div>
  </div>
  <div class="card active" style="left:455px">
    <div class="photo" role="img" aria-label="Portrait photo of a team member in an office" style="background:linear-gradient(135deg,#e8e4dc,#8a7060)"></div>
    <h5>Nora Hayes</h5><div class="role">Designer</div>
    <div class="socials"><span class="dot"></span><span class="dot"></span><span class="dot"></span></div>
  </div>
  <div class="card" style="left:769px">
    <div class="photo" role="img" aria-label="Portrait photo of a team member reviewing papers" style="background:linear-gradient(135deg,#8a7a6a,#e4e4e4)"></div>
    <h5>Owen Blake</h5><div class="role">Opreater</div>
  </div>
</section>

<footer class="footer">
  <div class="brand">REELPITCH.NET</div>
  <nav class="footer-nav"><span>Home</span><span>Features</span><span>Portfolio</span><span>News</span><span>Team</span><span>Products</span><span>Contact Us</span></nav>
  <div class="footer-social"><span></span><span></span><span></span></div>
</footer>
<div class="abs legal" style="left:0;width:1200px">© 2019 Reelpitch.net | Privacy Policy</div>

</body>
</html>
```